Postcard Design for Marketing to Builders

I am an architect that gets most of my work from contractor's. I design residential and commercial projects based in California. My main focus is California's Central Coast. I want the feel of the postcard to reflect a strong professional, efficient and creative partner for contractors (Builders). I have provide some photos of projects I have done recently to use on the postcard if needed. I have also included my logo which I would like on the front.

Industry/Entity Type

Architect

Font styles to use
Serif

```html
<!DOCTYPE html>
<html lang="en">
<head>
<meta charset="utf-8">
<title>Daniel R Hayes Architect – Postcard</title>
<link rel="stylesheet" href="https://fonts.googleapis.com/css2?family=Roboto+Condensed:wght@400;700&family=Open+Sans:wght@400;700&family=Lato:wght@400&display=swap">
<style>
  :root{
    --navy:#2b2a7c;
    --orange:#f26a21;
    --red-orange:#e9462a;
    --charcoal:#3b3b3d;
    --ink:#1f1f21;
    --paper:#ffffff;
    --backdrop:#ecebe8;
    --line:#c9c9cc;
  }
  *{box-sizing:border-box;margin:0;padding:0}
  html,body{width:907px;height:1200px;overflow:hidden;background:var(--backdrop)}
  .canvas{position:relative;width:907px;height:1200px}
  .postcard{position:absolute;width:716px;height:463px;background:var(--paper);overflow:hidden;box-shadow:0 4px 14px rgba(0,0,0,.18)}
  .postcard--front{left:96px;top:82px}
  .postcard--back{left:98px;top:636px}
  .postcard__art{position:absolute;inset:0;width:716px;height:463px}
  .brand{position:absolute;display:flex;align-items:center;gap:8px;font-family:"Roboto Condensed",sans-serif;font-weight:700;color:var(--navy);font-size:15px;letter-spacing:.5px;text-transform:uppercase}
  .brand__mark{width:16px;height:16px;background:var(--orange)}
  .postcard--front .brand{left:22px;top:60px}
  .headline{position:absolute;left:16px;top:100px;font-family:"Roboto Condensed",sans-serif}
  .headline__title{font-size:60px;font-weight:700;color:var(--ink);line-height:1;letter-spacing:-.5px}
  .headline__sub{margin-top:12px;font-size:33px;font-weight:400;color:var(--navy);line-height:1.05;text-transform:uppercase}
  .headline__place{margin-top:14px;font-family:"Open Sans",sans-serif;font-size:20px;font-weight:700;color:var(--red-orange);text-transform:uppercase}
  .contact{position:absolute;list-style:none;font-family:"Open Sans",sans-serif;font-size:15px;color:var(--paper)}
  .contact li{display:flex;align-items:center;gap:10px;height:24px}
  .contact svg{width:12px;height:12px;fill:var(--orange)}
  .postcard--front .contact{left:20px;top:368px}
  .postcard--back .contact{left:20px;top:386px;font-size:14px}
  .social{position:absolute;left:278px;top:419px;display:flex;align-items:center;gap:6px;font-family:"Open Sans",sans-serif;font-size:11px;color:var(--paper)}
  .social__dot{width:19px;height:19px;border-radius:50%;background:var(--orange)}
  .social span:first-child{margin-right:6px}
  .about-tab{position:absolute;left:0;top:18px;width:102px;height:22px;background:var(--navy);color:var(--paper);font-family:"Open Sans",sans-serif;font-size:15px;line-height:22px;padding-left:16px;clip-path:polygon(0 0,100% 0,94% 100%,0 100%)}
  .about-text{position:absolute;left:16px;top:48px;width:320px;font-family:"Lato",sans-serif;font-size:11px;line-height:13.6px;color:var(--ink);text-align:justify}
  .stamp-box{position:absolute;left:618px;top:68px;width:60px;height:78px;border:1px solid var(--line)}
  .address-line{position:absolute;left:458px;width:224px;height:1px;background:var(--line)}
  .postcard--back .brand{left:342px;top:392px;font-size:14px}
</style>
</head>
<body>
<div class="canvas">

  <!-- Front -->
  <section class="postcard postcard--front">
    <svg class="postcard__art" viewBox="0 0 716 463" aria-hidden="false">
      <defs>
        <linearGradient id="facadeTone" x1="0" y1="0" x2="0" y2="1">
          <stop offset="0" stop-color="#5a8fd6"/>
          <stop offset=".35" stop-color="#a9c3df"/>
          <stop offset=".5" stop-color="#d8d3bd"/>
          <stop offset="1" stop-color="#58605e"/>
        </linearGradient>
        <linearGradient id="timberTone" x1="0" y1="0" x2="0" y2="1">
          <stop offset="0" stop-color="#7b9fd1"/>
          <stop offset=".4" stop-color="#a8633d"/>
          <stop offset="1" stop-color="#7d6a59"/>
        </linearGradient>
        <linearGradient id="entryTone" x1="0" y1="0" x2="0" y2="1">
          <stop offset="0" stop-color="#9cc2ea"/>
          <stop offset=".5" stop-color="#ece3c3"/>
          <stop offset="1" stop-color="#6d8e4a"/>
        </linearGradient>
      </defs>
      <g role="img" aria-label="Photograph of a completed commercial building with a cupola and tall windows">
        <polygon points="345,0 716,0 716,360 430,360" fill="url(#facadeTone)"/>
      </g>
      <polygon points="316,0 342,0 424,320 404,320" fill="var(--navy)"/>
      <path d="M0,350 Q300,318 716,296 L716,463 L0,463 Z" fill="var(--charcoal)"/>
      <path d="M0,338 Q260,306 716,288 L716,300 Q300,320 0,350 Z" fill="var(--orange)"/>
      <path d="M0,330 Q250,300 716,280 L716,286 Q260,304 0,336 Z" fill="var(--navy)"/>
      <g role="img" aria-label="Photograph of a timber-framed entry with stone piers">
        <circle cx="443" cy="340" r="86" fill="var(--navy)"/>
        <circle cx="443" cy="340" r="80" fill="var(--paper)"/>
        <circle cx="443" cy="340" r="74" fill="url(#timberTone)"/>
      </g>
      <g role="img" aria-label="Photograph of a single-storey building entrance with landscaping">
        <circle cx="616" cy="360" r="74" fill="var(--navy)"/>
        <circle cx="616" cy="360" r="68" fill="var(--paper)"/>
        <circle cx="616" cy="360" r="62" fill="url(#entryTone)"/>
      </g>
    </svg>

    <div class="brand"><span class="brand__mark"></span>Daniel R Hayes Architect</div>

    <div class="headline">
      <h1 class="headline__title">Architect</h1>
      <p class="headline__sub">Of residential and<br>commercial projects</p>
      <p class="headline__place">Based in California</p>
    </div>

    <ul class="contact">
      <li><svg viewBox="0 0 12 12"><path d="M2.5 0.5l2 2.5-1 1.2c.7 1.5 1.8 2.6 3.3 3.3l1.2-1 2.5 2-1.2 2.4C4.7 10.6 1.4 7.3.1 1.7z"/></svg>0123456789</li>
      <li><svg viewBox="0 0 12 12"><path d="M0 2h12v1.2L6 7 0 3.2zM0 4.6l6 3.8 6-3.8V10H0z"/></svg>yourname@companyname.com</li>
      <li><svg viewBox="0 0 12 12"><circle cx="6" cy="6" r="6"/></svg>www.companyname.com</li>
    </ul>

    <div class="social"><span>Follow me on</span><span class="social__dot"></span><span class="social__dot"></span></div>
  </section>

  <!-- Back -->
  <section class="postcard postcard--back">
    <svg class="postcard__art" viewBox="0 0 716 463">
      <defs>
        <linearGradient id="officeTone" x1="0" y1="0" x2="0" y2="1">
          <stop offset="0" stop-color="#7eaee6"/>
          <stop offset=".5" stop-color="#c2a27d"/>
          <stop offset="1" stop-color="#7c8a64"/>
        </linearGradient>
        <linearGradient id="cottageTone" x1="0" y1="0" x2="0" y2="1">
          <stop offset="0" stop-color="#6f9d6a"/>
          <stop offset=".5" stop-color="#e6e8e4"/>
          <stop offset="1" stop-color="#b89e83"/>
        </linearGradient>
      </defs>
      <rect x="0" y="224" width="340" height="3" fill="var(--orange)"/>
      <g role="img" aria-label="Photograph of a three-storey office building">
        <rect x="0" y="230" width="184" height="126" fill="url(#officeTone)"/>
      </g>
      <g role="img" aria-label="Photograph of a two-storey cottage with exterior stairs">
        <rect x="188" y="230" width="160" height="126" fill="url(#cottageTone)"/>
      </g>
      <path d="M0,372 Q200,356 340,346 L340,463 L0,463 Z" fill="var(--charcoal)"/>
      <path d="M0,362 Q200,346 345,336 L345,346 Q200,356 0,372 Z" fill="var(--orange)"/>
      <path d="M0,356 Q200,340 345,330 L345,335 Q200,345 0,361 Z" fill="var(--navy)"/>
      <polygon points="394,0 410,0 328,463 318,463" fill="var(--orange)"/>
      <polygon points="410,0 428,0 336,463 328,463" fill="var(--navy)"/>
    </svg>

    <div class="about-tab">About Me</div>
    <p class="about-text">Lorem ipsum dolor sit amet, consectetuer adipiscing elit. Aenean commodo ligula eget dolor. Aenean massa. Cum sociis natoque penatibus et magnis dis parturient montes, nascetur ridiculus mus. Donec quam felis, ultricies nec, pellentesque eu, pretium quis, sem. Nulla consequat massa quis enim. Donec pede justo, fringilla vel, aliquet nec, vulputate eget, arcu. In enim justo, rhoncus ut, imperdiet a, venenatis vitae, justo. Nullam dictum felis eu pede mollis pretium. Integer tincidunt. Cras dapibus. Vivamus elementum semper nisi. Aenean vulputate eleifend tellus. Aenean leo ligula, porttitor eu, consequat vitae, eleifend ac, enim. Aliquam lorem ante, dapibus in, viverra quis, feugiat a, tellus. Phasellus viverra nulla ut metus varius laoreet. Quisque rutrum.</p>

    <ul class="contact">
      <li><svg viewBox="0 0 12 12"><path d="M2.5 0.5l2 2.5-1 1.2c.7 1.5 1.8 2.6 3.3 3.3l1.2-1 2.5 2-1.2 2.4C4.7 10.6 1.4 7.3.1 1.7z"/></svg>0123456789</li>
      <li><svg viewBox="0 0 12 12"><path d="M0 2h12v1.2L6 7 0 3.2zM0 4.6l6 3.8 6-3.8V10H0z"/></svg>yourname@companyname.com</li>
      <li><svg viewBox="0 0 12 12"><circle cx="6" cy="6" r="6"/></svg>www.companyname.com</li>
    </ul>

    <div class="stamp-box"></div>
    <div class="address-line" style="top:223px"></div>
    <div class="address-line" style="top:262px"></div>
    <div class="address-line" style="top:300px"></div>

    <div class="brand"><span class="brand__mark"></span>Daniel R Hayes Architect</div>
  </section>

</div>
</body>
</html>
```